Private Dining Restaurant Menu Design

Looking for help in designing a private dining room menu brochure - probably would need 4 panel layout to make all of the content fit, or a 5.5x8" booklet. Open to your ideas on layout/vessel - would want to post on website and be able to print to hand out to guests interested in booking our private dining room.

All content is in the attached "Private Dining Menu".

Would like to match existing dinner menu design - also attached.

Website is www.copperfernkitchen.com

Requirements
Must have
• Easy to read format of a brochure of the private dining menu content - want to be able to hand out to interested guests and have it simple and easy to read/flip through.

```html
<!DOCTYPE html>
<html lang="en">
<head>
<meta charset="utf-8">
<title>Copper Fern Kitchen – Sandwiches, Tacos &amp; Brick Oven Pizza</title>
<link href="https://fonts.googleapis.com/css2?family=Archivo+Black&family=Roboto:wght@400;700;900&display=swap" rel="stylesheet">
<style>
  :root {
    --page-bg: #efe9e2;
    --menu-red: #d8281a;
    --band-gold: #f2bd3c;
    --heading-red: #c4200f;
    --text-white: #ffffff;
    --text-soft: #fbe3dc;
    --photo-warm: #8a5a3c;
    --photo-green: #6f7d3a;
    --photo-gold: #d8a84a;
  }
  * { box-sizing: border-box; margin: 0; padding: 0; }
  html, body { width: 1200px; height: 1200px; overflow: hidden; }
  body { background: var(--page-bg); font-family: "Roboto", Arial, sans-serif; }

  .menu-sheet {
    position: absolute; left: 190px; top: 30px;
    width: 820px; height: 1140px;
    box-shadow: 0 10px 30px rgba(0,0,0,.25);
    overflow: hidden;
  }
  .food-photo {
    position: absolute; inset: 0;
    background:
      radial-gradient(circle at 80% 12%, #c9322a 0 8%, transparent 20%),
      radial-gradient(circle at 15% 40%, var(--photo-warm) 0 20%, transparent 45%),
      radial-gradient(circle at 85% 70%, var(--photo-gold) 0 10%, transparent 30%),
      radial-gradient(circle at 40% 95%, var(--photo-green) 0 15%, transparent 35%),
      linear-gradient(160deg, #9a7a5e, #6e5443 50%, #8c7a5a);
  }
  .menu-panel {
    position: absolute; left: 40px; top: 60px;
    width: 750px;
    background: linear-gradient(180deg, rgba(216,40,26,.94), rgba(200,34,20,.94));
    padding: 0 0 30px;
  }
  .section-band {
    background: var(--band-gold);
    height: 56px;
    display: flex; align-items: center; justify-content: center;
    margin-bottom: 16px;
  }
  .section-band h2 {
    font-family: "Archivo Black", "Arial Black", sans-serif;
    font-weight: 400;
    color: var(--heading-red);
    font-size: 32px; letter-spacing: .5px;
  }
  .section + .section { margin-top: 18px; }
  .item-list { list-style: none; padding: 0 34px; }
  .menu-item {
    display: grid; grid-template-columns: 1fr auto;
    column-gap: 14px; margin-bottom: 11px;
    color: var(--text-white);
  }
  .item-name {
    font-weight: 900; font-size: 21px; letter-spacing: .4px;
    text-transform: uppercase; line-height: 1.15;
  }
  .item-price {
    text-align: right; font-weight: 700; font-size: 19px; line-height: 1.2;
  }
  .item-desc {
    grid-column: 1 / 3;
    font-size: 15px; line-height: 1.3; color: var(--text-soft);
  }
  .topping-line {
    font-size: 15px; line-height: 1.35; color: var(--text-soft);
  }
  .topping-price {
    text-align: right; font-weight: 700; font-size: 17px; line-height: 1.2;
  }
</style>
</head>
<body>
  <article class="menu-sheet">
    <div class="food-photo" role="img" aria-label="Blurred photograph of grilled meats, peppers and vegetables behind the menu"></div>

    <div class="menu-panel">
      <section class="section">
        <header class="section-band"><h2>SANDWICHES &amp; TACOS</h2></header>
        <ul class="item-list">
          <li class="menu-item"><span class="item-name">Chicago Steak Sandwich</span><span class="item-price">15</span>
            <p class="item-desc">Ribeye shaved thin &amp; grilled with giardanera &amp; cheese sauce. Served with au jus for dipping.</p></li>
          <li class="menu-item"><span class="item-name">Chicken Tacos</span><span class="item-price">11</span>
            <p class="item-desc">Grilled tacos filled with rotisserie chicken, black beans, roasted corn salsa, pico, lettuce &amp; chipotle</p></li>
          <li class="menu-item"><span class="item-name">Walleye Tacos</span><span class="item-price">13</span>
            <p class="item-desc">Your choice of Blackened or Lakeside Crisp Breaded walleye with green cabbage, mozzarella,</p></li>
          <li class="menu-item"><span class="item-name">House Smoked BBQ Pork</span><span class="item-price">10</span>
            <p class="item-desc">Topped with creamy cole slaw on a buttered bun.</p></li>
          <li class="menu-item"><span class="item-name">Avocado Bacon Rotisserie</span><span class="item-price">13</span>
            <p class="item-desc">Chicken, avocado, thick-cut bacon, provolone, ranch dressing, tomato &amp; spring mix.</p></li>
          <li class="menu-item"><span class="item-name">Pepper Jack Turkey Melt</span><span class="item-price">13</span>
            <p class="item-desc">Thick-cut bacon, lettuce, vine ripened tomato &amp; spicy mayo on a pretzel bun.</p></li>
          <li class="menu-item"><span class="item-name">Walleye Sandwich</span><span class="item-price">14</span>
            <p class="item-desc">Lemon herb aioli, field greens, tomatoes &amp; pickles.</p></li>
          <li class="menu-item"><span class="item-name">Southwest Spiced-Chicken Sandwich</span><span class="item-price">11</span>
            <p class="item-desc">Seasoned wood-roasted chicken, peppers, pickled jalapeños, onions, pepper jack cheese &amp; spicy mayo on ciabatta bread.</p></li>
        </ul>
      </section>

      <section class="section">
        <header class="section-band"><h2>BRICK OVEN PIZZA</h2></header>
        <ul class="item-list">
          <li class="menu-item"><span class="item-name">Build Your Own</span><span class="item-price">9</span>
            <p class="item-desc">House shredded mozzarella and house tomato sauce with your choice of toppings.</p></li>
          <li class="menu-item"><span class="item-name">The Double Pepperoni</span><span class="item-price">12</span>
            <p class="item-desc">House made pizza sauce, jumbo sliced pepperoni, diced pepperoni, mozzarella &amp; fresh herbs.</p></li>
          <li class="menu-item"><span class="item-name">BBQ Chicken</span><span class="item-price">12</span>
            <p class="item-desc">Rotisserie BBQ chicken with red onions, green peppers, cheddar &amp; jack cheeses.</p></li>
          <li class="menu-item"><span class="item-name">Sausage &amp; Mushroom</span><span class="item-price">12</span>
            <p class="item-desc">House made fennel sausage with fresh mushrooms, mozzarella, tomato sauce &amp; fresh basil.</p></li>
          <li class="menu-item"><span class="item-name">The Works</span><span class="item-price">13</span>
            <p class="item-desc">Pepperoni, sausage, green pepper, chopped green olives, mushrooms &amp; onions.</p></li>
          <li class="menu-item">
            <span class="item-name">Each Additional Topping</span><span></span>
            <span class="topping-line">Rotisserie chicken • Pepperoni • Bacon • Italian sausage</span><span class="topping-price">2 Each</span>
            <span class="topping-line">Mushroom • Green pepper • Pineapple • Jalapeño • Red pepper • Red onion • Chopped green olives</span><span class="topping-price">1 Each</span>
          </li>
        </ul>
      </section>
    </div>
  </article>
</body>
</html>
```